Wedding Day Custom Wine Label - Tasmanian (Tamar Valley) wine

I am looking for a custom design that will be put on a wine label to commemorate a very good friend's wedding day.

We will need to be able to take the design and print it on to sticker labels that we can put on to wine bottles.

The bride and groom have asked for a simplistic label design (see example image attached). We need two labels. One for "Pinot Noir" wine and the other for "Chardonnay" wine. We would like the label to say:

The Hartwell's
Pinot Noir
2023
Tamar Valley

and for for the other wine variety:

The Hartwell's
Chardonnay
2023
Tamar Valley

smaller text below to say:

13.5% ALC/VOL 750ML
MEGAN & LIAM - 31.10.2024

I am happy to consider other variations - the bride & groom would prefer something minimalistic. Elegant and classy.

Target Market(s)

the bride & groom

Requirements
Must have
• Wedding date (31.10.2024). Wine type (Pinot Noir or Chardonnay).
Should not have
• images not essential

```html
<!DOCTYPE html>
<html lang="en">
<head>
<meta charset="utf-8">
<title>The Hartwell's – Wedding Wine Labels</title>
<link rel="stylesheet" href="https://fonts.googleapis.com/css2?family=Montserrat:wght@300;500;600;800&display=swap">
<style>
  :root {
    --backdrop: #230307;
    --label-paper: #f6f4ea;
    --ink: #1b1a1a;
    --ink-soft: #4a4846;
    --rose-band: #d4aaa4;
    --rose-accent: #9a4a4c;
    --gold-band: #ecdcae;
    --gold-accent: #b8902f;
  }
  * { margin: 0; padding: 0; box-sizing: border-box; }
  html, body {
    width: 1200px;
    height: 1200px;
    overflow: hidden;
    background: var(--backdrop);
    font-family: "Montserrat", Arial, sans-serif;
  }
  .canvas {
    position: relative;
    width: 1200px;
    height: 1200px;
  }
  .label {
    position: absolute;
    top: 343px;
    width: 500px;
    height: 513px;
    background: var(--label-paper);
    color: var(--ink);
  }
  .label--pinot { left: 70px; --accent: var(--gold-accent); --band: var(--gold-band); }
  .label--chardonnay { left: 630px; --accent: var(--rose-accent); --band: var(--rose-band); }

  .label__band {
    position: absolute;
    left: 0;
    top: 0;
    width: 89px;
    height: 100%;
    background: linear-gradient(to bottom, var(--band) 0%, var(--band) 55%, var(--label-paper) 100%);
  }
  .label__house {
    position: absolute;
    left: 202px;
    top: 195px;
    font-weight: 800;
    font-size: 31px;
    line-height: 27px;
    letter-spacing: 1.5px;
    text-transform: uppercase;
  }
  .label__marker {
    position: absolute;
    left: 199px;
    top: 325px;
    width: 26px;
    height: 7px;
    background: var(--accent);
  }
  .label__variety {
    position: absolute;
    left: 195px;
    top: 342px;
    font-weight: 800;
    font-size: 20px;
    letter-spacing: 0.6px;
    text-transform: uppercase;
  }
  .label__region {
    position: absolute;
    left: 197px;
    top: 373px;
    font-weight: 500;
    font-size: 16px;
    letter-spacing: 2.6px;
    text-transform: uppercase;
    color: var(--ink-soft);
  }
  .label__vintage {
    position: absolute;
    left: 420px;
    top: 378px;
    transform: translate(-50%, -50%) rotate(-90deg);
    font-weight: 300;
    font-size: 18px;
    letter-spacing: 2px;
    color: var(--accent);
  }
  .label__specs {
    position: absolute;
    left: 194px;
    top: 452px;
    width: 228px;
    display: flex;
    justify-content: space-between;
    font-weight: 300;
    font-size: 10px;
    letter-spacing: 2.4px;
    color: var(--ink-soft);
  }
  .label__couple {
    position: absolute;
    left: 194px;
    top: 470px;
    font-weight: 600;
    font-size: 11.5px;
    letter-spacing: 1.6px;
    text-transform: uppercase;
  }
</style>
</head>
<body>
<main class="canvas">
  <article class="label label--pinot">
    <div class="label__band" role="img" aria-label="Soft gold band of fine wavy contour lines"></div>
    <h1 class="label__house">The<br>Hartwell’s</h1>
    <span class="label__marker"></span>
    <h2 class="label__variety">Pinot Noir</h2>
    <p class="label__region">Tamar Valley</p>
    <p class="label__vintage">2023</p>
    <p class="label__specs"><span>13.5% ALC/VOL</span><span>750ML</span></p>
    <p class="label__couple">Megan &amp; Liam - 31.10.2024</p>
  </article>

  <article class="label label--chardonnay">
    <div class="label__band" role="img" aria-label="Soft rose band of fine wavy contour lines"></div>
    <h1 class="label__house">The<br>Hartwell’s</h1>
    <span class="label__marker"></span>
    <h2 class="label__variety">Chardonnay</h2>
    <p class="label__region">Tamar Valley</p>
    <p class="label__vintage">2023</p>
    <p class="label__specs"><span>13.5% ALC/VOL</span><span>750ML</span></p>
    <p class="label__couple">Megan &amp; Liam - 31.10.2024</p>
  </article>
</main>
</body>
</html>
```